The website is called gearvorn.net. It's a DIY projects ( only mechanical engineering related projects ) where mechanical engineers/student can share their ideas/ DIY projects/tutorial/course projects/Graduation projects...etc.
The website is more or less like craftlumen.net ( please spend some time in this website ), but strictly to mechanical engineer and it will feature projects like pumps, turbines, compressor, gearboxes, automotive ...etc
There will be four categories:
1- Create, it's where the user can share his project, so it will have a writing feature ( title, body , upload image at different locations of the body ...etc)
2- Tutorials, where is user can share a tutorial so it should have a writing feature also
3- Build, where the user can see others projects
4- Buy, two items: a- T-shirts, b-Books ( DIY books made by us )
Notes:
-In the Share and tutorial categories, the user should select subcategory ( Will give them to you later ).
-When clicking to "make" category the user can see all the posted projects, then he can select a sub category ( see partwisp.net )
- each user will have a personal page
- Buy category will be added later if the website succeeded
- landing page feature the latest projects,tutorial
This is the full detail about the website, if there is something specific please let me know.
*No logo is been made yet.
thanks.
Industry/Entity Type
Mechanical Engineering

```html
<!DOCTYPE html>
<html lang="en">
<head>
<meta charset="utf-8">
<title>gearvorn.net — DIY Mechanical Projects</title>
<link href="https://fonts.googleapis.com/css2?family=Oswald:wght@400;500;600&family=Open+Sans:ital,wght@0,400;0,600;1,400&display=swap" rel="stylesheet">
<style>
:root{
  --orange:#f7770f;
  --orange-light:#ff9a3c;
  --ink:#1b1b1b;
  --dark:#3a3a3a;
  --footer:#414141;
  --grey-bg:#e2e2e2;
  --panel:#ffffff;
  --muted:#666;
  --red:#c0261d;
  --line:#d7d7d7;
}
*{box-sizing:border-box;margin:0;padding:0}
html,body{width:898px;height:1200px;overflow:hidden}
body{position:relative;background:#fff;font-family:"Open Sans",Arial,sans-serif;color:var(--dark)}
.abs{position:absolute}
.header{left:0;top:0;width:898px;height:66px;background:var(--grey-bg)}
.brand{left:100px;top:16px;font-family:"Oswald",sans-serif;font-weight:600;font-size:24px;letter-spacing:.3px;color:var(--ink)}
.brand-mark{display:inline-block;width:12px;height:12px;background:var(--orange);margin-left:6px;vertical-align:middle}
.utility{left:646px;top:0;width:155px;height:29px;background:#fff;border:1px solid #ccc;border-top:none;border-radius:0 0 8px 8px;font-size:9px;color:#222;display:flex;justify-content:center;align-items:center;gap:6px}
.utility span.sep{color:#777}
.nav{left:0;top:69px;width:898px;height:41px;background:linear-gradient(#ff8a26,var(--orange) 55%,#f26a05)}
.nav-list{left:92px;top:69px;height:41px;display:flex;list-style:none;font-size:10px;color:#fff}
.nav-list li{height:41px;line-height:41px;padding:0 13px;border-right:1px solid rgba(255,255,255,.35)}
.nav-list li.active{background:#111;padding:0 14px 0 22px;border:none}
.nav-list li:last-child{border:none}
.search{left:576px;top:77px;width:167px;height:22px;background:#fff;border:none}
.search-btn{left:743px;top:77px;width:60px;height:22px;background:#151515;color:#fff;font-size:9px;text-align:center;line-height:22px}
.stage{left:0;top:110px;width:898px;height:288px;background:linear-gradient(#d8d8d8,#e4e4e4);border-top:3px solid #ececec}
.slider{left:93px;top:122px;width:708px;height:247px;background:#2c3138;border:1px solid #111;box-shadow:0 14px 18px -10px rgba(0,0,0,.45)}
.slide-photo{left:104px;top:132px;width:685px;height:226px;background:linear-gradient(100deg,#6e7d8c 0%,#a9b4c0 35%,#dfe4ea 60%,#b5bcc6 85%,#7c6fa6 100%)}
.caption{left:94px;top:211px;width:260px;height:83px;background:rgba(40,40,40,.8);border-bottom:3px solid var(--orange);padding:8px 16px;color:#fff}
.caption h2{font-family:"Oswald",sans-serif;font-weight:500;font-size:13px;margin-bottom:4px}
.caption p{font-size:9px;line-height:13px}
.dots{left:372px;top:377px;width:131px;height:21px;background:linear-gradient(#f3f5f8,#d9dee5);border:1px solid #aab;border-radius:4px;display:flex;justify-content:center;align-items:center;gap:7px}
.dots i{width:6px;height:6px;border-radius:50%;background:#8d97a3}
.dots i.on{background:#222}
.feature{width:140px;height:140px;border-radius:50%;overflow:hidden;background:linear-gradient(#fff,#e6e6e6);border:3px solid #fff;box-shadow:0 0 0 1px #ddd,0 2px 4px rgba(0,0,0,.15);text-align:center}
.feature h3{background:var(--orange);height:40px;line-height:46px;color:#fff;font-family:"Oswald",sans-serif;font-weight:500;font-size:16px}
.feature p{height:68px;display:flex;align-items:center;justify-content:center;padding:0 10px;font-size:11px;line-height:14px;color:#333}
.feature a{display:block;height:32px;background:#1d1d1d;color:#fff;font-size:10.5px;line-height:20px;text-decoration:none}
.box{background:var(--panel);border:1px solid #e4e4e4;box-shadow:0 6px 8px -6px rgba(0,0,0,.35)}
.box-title{font-family:"Oswald",sans-serif;font-weight:500;font-size:14px;color:var(--ink);padding:8px 15px 6px;border-bottom:1px solid #e8e8e8}
.arrows{position:absolute;right:14px;top:8px;color:#999;font-size:12px;letter-spacing:6px}
.proj{position:absolute;left:14px;width:200px}
.thumb{position:absolute;left:0;top:0;width:66px;height:75px;border-radius:7px}
.proj-date{position:absolute;left:75px;top:0;font-size:9px;color:var(--red)}
.proj-text{position:absolute;left:77px;top:16px;width:124px;font-size:8px;line-height:10px;color:#777;text-align:justify}
.more{position:absolute;font-size:8.5px;color:var(--red)}
.cats{list-style:none;position:absolute;left:18px;top:52px;width:200px}
.cats li{position:relative;padding-left:14px;font-size:8px;line-height:10px;color:#555;margin-bottom:11px}
.cats li::before{content:"›";position:absolute;left:2px;top:-2px;font-size:11px;color:#333}
.tut-heading{left:348px;top:593px;width:448px;font-family:"Oswald",sans-serif;font-weight:500;font-size:15px;color:#333;border-bottom:1px solid #ccc;padding-bottom:2px}
.tut{position:absolute;left:350px;width:446px;height:100px}
.tut-img{position:absolute;left:0;top:0;width:122px;height:77px;border:2px solid #bbb}
.tut h4{position:absolute;left:130px;top:0;font-weight:400;font-size:10px;color:var(--red)}
.tut time{position:absolute;left:130px;top:17px;font-size:8px;color:#444}
.tut p{position:absolute;left:130px;top:29px;width:316px;font-size:8px;line-height:12px;color:#555}
.learn{position:absolute;left:378px;top:72px;width:60px;height:23px;background:#3d3d3d;color:#fff;font-family:"Oswald",sans-serif;font-size:10px;text-align:center;line-height:23px}
.pager{left:692px;top:1069px;display:flex;gap:12px;align-items:center;font-size:13px;color:#222}
.pager .cur{width:23px;height:23px;border-radius:50%;background:var(--orange);text-align:center;line-height:23px}
.rule{left:62px;top:1102px;width:770px;border-top:1px dotted #999}
.footer{left:0;top:1104px;width:898px;height:96px;background:var(--footer)}
.nl-title{left:100px;top:1123px;font-family:"Oswald",sans-serif;font-size:12px;color:#fff}
.nl-input{left:98px;top:1150px;width:204px;height:20px;background:#fff;border:1px solid #ccc;font-size:8px;font-style:italic;color:#999;padding:4px 8px}
.nl-btn{left:315px;top:1150px;width:64px;height:20px;background:linear-gradient(#f2f2f2,#cfcfcf);border-radius:3px;font-size:9.5px;font-weight:600;color:#333;text-align:center;line-height:20px}
.social{left:709px;top:1133px;display:flex;gap:10px}
.social i{width:18px;height:18px;display:block}
.copy{right:84px;top:1163px;font-size:8.5px;color:#eee}
</style>
</head>
<body>
<header>
  <div class="abs header"></div>
  <div class="abs brand">GEARVORN<span class="brand-mark"></span></div>
  <div class="abs utility"><span>Help</span><span class="sep">|</span><span>Login</span><span class="sep">|</span><span>Register</span></div>
  <div class="abs nav"></div>
  <ul class="abs nav-list">
    <li class="active">HOME</li><li>ABOUT US</li><li>SERVICES</li><li>EXPERTS</li><li>TUTORIALS</li><li>PROJECTS</li>
  </ul>
  <div class="abs search"></div>
  <div class="abs search-btn">SEARCH</div>
</header>

<section>
  <div class="abs stage"></div>
  <div class="abs slider"></div>
  <div class="abs slide-photo" role="img" aria-label="Photo of students working on mechanical equipment in a lab"></div>
  <div class="abs caption">
    <h2>LOREM IPSUM DOLOR SIT AMET, ELIT</h2>
    <p>Cum sociis natoque penatibus et magnis dis parturient montes, nascetur ridiculus mus. In iaculis facilisis massa. Etiam eu urna.</p>
  </div>
  <div class="abs dots"><i></i><i></i><i class="on"></i><i></i><i></i><i></i></div>
</section>

<section>
  <div class="abs feature" style="left:97px;top:428px"><h3>CREATE</h3><p>where users can share their projects or create and upload images</p><a>Share Project</a></div>
  <div class="abs feature" style="left:285px;top:428px"><h3>TUTORIALS</h3><p>where users can share their documents and tutorials</p><a>Upload Project</a></div>
  <div class="abs feature" style="left:473px;top:428px"><h3>BUILD</h3><p>where users can see other projects</p><a>View Project</a></div>
  <div class="abs feature" style="left:653px;top:428px"><h3>BUY</h3><p>we have 2 items for sale, 1 - Tshirt and 2 - DIY book which we had compiled</p><a>Buy Now</a></div>
</section>

<aside>
  <div class="abs box" style="left:93px;top:596px;width:225px;height:234px">
    <div class="box-title">LATEST PROJECTS</div><span class="arrows">‹›</span>
    <div class="proj" style="top:40px">
      <div class="thumb" role="img" aria-label="Photo of a hand-built engine project" style="background:linear-gradient(135deg,#3b4350,#8a8f96)"></div>
      <div class="proj-date">Mar 23 2013</div>
      <p class="proj-text">Sed ut perspiciatis unde omnis iste natus error sit voluptatem accusantiumveritatis et quasi.sit voluptatem accusantiumveritatis et quasi.</p>
      <span class="more" style="left:144px;top:70px">Read More &gt;&gt;</span>
    </div>
    <div class="proj" style="top:134px">
      <div class="thumb" role="img" aria-label="Photo of a wind turbine project under a cloudy sky" style="background:linear-gradient(#5f86b8,#c7d5e4)"></div>
      <div class="proj-date">Mar 23 2013</div>
      <p class="proj-text">Sed ut perspiciatis unde omnis iste natus error sit voluptatem accusantiumveritatis et quasi.sit voluptatem accusantiumveritatis et quasi.</p>
      <span class="more" style="left:144px;top:70px">Read More &gt;&gt;</span>
    </div>
  </div>

  <div class="abs box" style="left:93px;top:850px;width:225px;height:234px">
    <div class="box-title">PROJECT CATEGORIES</div>
    <ul class="cats" style="top:42px">
      <li>Sed ut perspiciatis unde omnis iste natus error sit voluptatem accusantiumveritatis et quasi.</li>
      <li>Sed ut perspiciatis unde omnis iste natus error sit voluptatem accusantiumveritatis et quasi.</li>
      <li>Sed ut perspiciatis unde omnis iste natus error sit voluptatem accusantiumveritatis et quasi.</li>
      <li>Sed ut perspiciatis unde omnis iste natus error sit voluptatem accusantiumveritatis et quasi.</li>
      <li>Sed ut perspiciatis unde omnis iste natus error sit voluptatem accusantiumveritatis et quasi.</li>
    </ul>
    <span class="more" style="left:152px;top:207px">Read More &gt;&gt;</span>
  </div>
</aside>

<main>
  <h2 class="abs tut-heading">LATEST TUTORIALS</h2>
  <article class="tut" style="top:628px">
    <div class="tut-img" role="img" aria-label="Photo of a vacuum pump" style="background:linear-gradient(135deg,#e8e8e8,#7d8790)"></div>
    <h4>Excepteur sint occaecat.</h4><time>Mar 23 , 2013</time>
    <p>Sed ut perspiciatis unde omnis iste natus error sit accud ut perspiciatis unde omnis iste natus error sit voluptatem accusantium doloremque laudantium.ed ut perspicia-tis unde omnis iste natus error sit voluptatem accusantium doloremque laudantium.</p>
    <span class="learn">learn more</span>
  </article>
  <article class="tut" style="top:734px">
    <div class="tut-img" role="img" aria-label="Photo of wind turbines against a blue sky" style="background:linear-gradient(#3f6fb0,#cfdbe8)"></div>
    <h4>Excepteur sint occaecat.</h4><time>Mar 23 , 2013</time>
    <p>Sed ut perspiciatis unde omnis iste natus error sit accud ut perspiciatis unde omnis iste natus error sit voluptatem accusantium doloremque laudantium.ed ut perspicia-tis unde omnis iste natus error sit voluptatem accusantium doloremque laudantium.</p>
    <span class="learn">learn more</span>
  </article>
  <article class="tut" style="top:846px">
    <div class="tut-img" role="img" aria-label="Photo of an industrial air compressor" style="background:linear-gradient(135deg,#55595f,#1e2226)"></div>
    <h4>Excepteur sint occaecat.</h4><time>Mar 23 , 2013</time>
    <p>Sed ut perspiciatis unde omnis iste natus error sit accud ut perspiciatis unde omnis iste natus error sit voluptatem accusantium doloremque laudantium.ed ut perspicia-tis unde omnis iste natus error sit voluptatem accusantium doloremque laudantium.</p>
    <span class="learn">learn more</span>
  </article>
  <article class="tut" style="top:952px">
    <div class="tut-img" role="img" aria-label="Photo of a racing car engine bay" style="background:linear-gradient(135deg,#8c8c8c,#2a2a2a)"></div>
    <h4>Excepteur sint occaecat.</h4><time>Mar 23 , 2013</time>
    <p>Sed ut perspiciatis unde omnis iste natus error sit accud ut perspiciatis unde omnis iste natus error sit voluptatem accusantium doloremque laudantium.ed ut perspicia-tis unde omnis iste natus error sit voluptatem accusantium doloremque laudantium.</p>
    <span class="learn">learn more</span>
  </article>
  <nav class="abs pager"><span class="cur">1</span><span>2</span><span>3</span><span>10</span></nav>
</main>

<footer>
  <div class="abs rule"></div>
  <div class="abs footer"></div>
  <div class="abs nl-title">Newsletter</div>
  <div class="abs nl-input">your email address here..</div>
  <div class="abs nl-btn">Subscribe ›</div>
  <div class="abs social">
    <i style="background:#3b5998"></i><i style="background:#2ea5d9"></i><i style="background:#1f7bb6"></i><i style="background:#f39322"></i>
  </div>
  <div class="abs copy">© 2013 gearvorn.net, All Rights Reserved</div>
</footer>
</body>
</html>
```